Stationery + Biz Cards for an online geek store
Vicente Moraes
Stationery + Biz Cards for an online geek store - Hobbies
Creative Brief
Use same font as used in my logo
Try to use the same font if possible
Professional
General Manager
Rua Benedita, 542 - casa 11, 04317-020 - São Paulo - SP
vicente.moraes@nerdpraca.com.br
www.nerdpraca.com.br
Logo + Website www.nerdpraca.com.br

```html
<!DOCTYPE html>
<html lang="pt-BR">
<head>
<meta charset="utf-8">
<title>Nerdpraca – Business Card</title>
<link rel="stylesheet" href="https://fonts.googleapis.com/css2?family=Open+Sans:wght@400;600;700&display=swap">
<style>
  :root {
    --page-bg: #e9e7e3;
    --lime: #a4d65e;
    --lime-light: #b4e06e;
    --ink: #1c1c1c;
    --panel: #1a1a1a;
    --stripe: #8a8a8a;
    --text: #2e2e2e;
    --brand: #9fd24d;
  }
  * { margin: 0; padding: 0; box-sizing: border-box; }
  html, body {
    width: 1200px; height: 914px; overflow: hidden;
    background: var(--page-bg);
    font-family: "Open Sans", Arial, sans-serif;
  }
  .business-card {
    position: absolute; left: 50px; top: 137px;
    width: 1100px; height: 640px;
    background: linear-gradient(135deg, var(--lime-light), var(--lime));
    overflow: hidden;
    box-shadow: 0 10px 30px rgba(0,0,0,.18);
  }
  .card-shapes { position: absolute; inset: 0; }
  .holder { position: absolute; left: 150px; top: 78px; color: var(--text); }
  .holder-name { font-size: 30px; font-weight: 700; line-height: 1.2; }
  .holder-role { font-size: 22px; font-weight: 400; }
  .contact-list {
    position: absolute; left: 90px; top: 270px;
    list-style: none; color: var(--text); font-size: 20px; line-height: 1.3;
  }
  .contact-item { display: flex; align-items: flex-start; gap: 14px; margin-bottom: 8px; }
  .contact-icon {
    flex: none; width: 26px; height: 26px; border-radius: 50%;
    background: var(--ink); display: flex; align-items: center; justify-content: center;
    margin-top: 1px;
  }
  .contact-icon svg { width: 15px; height: 15px; fill: var(--lime); }
  .brand {
    position: absolute; left: 600px; top: 280px;
    display: flex; align-items: center; gap: 20px;
  }
  .brand-dot { width: 56px; height: 56px; border-radius: 50%; background: var(--brand); }
  .brand-name { font-size: 72px; font-weight: 600; color: var(--brand); letter-spacing: -1px; }
</style>
</head>
<body>
  <div class="business-card">
    <svg class="card-shapes" viewBox="0 0 1100 640" preserveAspectRatio="none" aria-hidden="true">
      <path d="M650 0 C540 120 450 320 440 640 L1100 640 L1100 0 Z" fill="var(--stripe)"/>
      <path d="M676 0 C566 120 476 320 466 640 L1100 640 L1100 0 Z" fill="var(--panel)"/>
    </svg>

    <div class="holder">
      <p class="holder-name">Vicente Moraes</p>
      <p class="holder-role">General Manager</p>
    </div>

    <ul class="contact-list">
      <li class="contact-item">
        <span class="contact-icon"><svg viewBox="0 0 24 24"><path d="M12 2a7 7 0 0 0-7 7c0 5 7 13 7 13s7-8 7-13a7 7 0 0 0-7-7zm0 9.5A2.5 2.5 0 1 1 12 6.5a2.5 2.5 0 0 1 0 5z"/></svg></span>
        <span>Rua Benedita, 542 - casa 11,<br>04317-020 - São Paulo - SP</span>
      </li>
      <li class="contact-item">
        <span class="contact-icon"><svg viewBox="0 0 24 24"><path d="M6.6 10.8a15 15 0 0 0 6.6 6.6l2.2-2.2a1 1 0 0 1 1-.25 11.4 11.4 0 0 0 3.6.57 1 1 0 0 1 1 1V20a1 1 0 0 1-1 1A17 17 0 0 1 3 4a1 1 0 0 1 1-1h3.5a1 1 0 0 1 1 1c0 1.25.2 2.45.57 3.57a1 1 0 0 1-.25 1z"/></svg></span>
        <span>+55 11 3471-2096</span>
      </li>
      <li class="contact-item">
        <span class="contact-icon"><svg viewBox="0 0 24 24"><path d="M7 1h10a2 2 0 0 1 2 2v18a2 2 0 0 1-2 2H7a2 2 0 0 1-2-2V3a2 2 0 0 1 2-2zm0 3v14h10V4zm5 15.5a1 1 0 1 0 0 2 1 1 0 0 0 0-2z"/></svg></span>
        <span>+55 11 9-8152-6340</span>
      </li>
      <li class="contact-item">
        <span class="contact-icon"><svg viewBox="0 0 24 24"><path d="M3 5h18v14H3zm2 2v.5l7 4.5 7-4.5V7zm0 2.8V17h14V9.8l-7 4.5z"/></svg></span>
        <span>vicente.moraes@nerdpraca.com.br</span>
      </li>
      <li class="contact-item">
        <span class="contact-icon"><svg viewBox="0 0 24 24"><path d="M12 2a10 10 0 1 0 0 20 10 10 0 0 0 0-20zm6.9 9h-3a15 15 0 0 0-1.3-5.6A8 8 0 0 1 18.9 11zM12 4.1c.9 1.3 1.8 3.6 1.9 6.9h-3.8C10.2 7.7 11.1 5.4 12 4.1zM9.4 5.4A15 15 0 0 0 8.1 11h-3a8 8 0 0 1 4.3-5.6zM5.1 13h3a15 15 0 0 0 1.3 5.6A8 8 0 0 1 5.1 13zm6.9 6.9c-.9-1.3-1.8-3.6-1.9-6.9h3.8c-.1 3.3-1 5.6-1.9 6.9zm2.6-1.3a15 15 0 0 0 1.3-5.6h3a8 8 0 0 1-4.3 5.6z"/></svg></span>
        <span>www.nerdpraca.com.br</span>
      </li>
    </ul>

    <div class="brand">
      <span class="brand-dot"></span>
      <span class="brand-name">nerdpraca</span>
    </div>
  </div>
</body>
</html>
```